Brindlewood Property Management, L.L.C
Brindlewood Property Management, L.L.C - Financial Services
Creative Brief
Professional
Doreen Whitlock,CAM
President
P.O. Box 572816 Naples, FL. 34117
info@brindlewoodprop.com
www.brindlewoodprop.com
I am open to clear business cards or two sides if a two sided design is used see comment below.
Logo on back of card if this option is designed

```html
<!DOCTYPE html>
<html lang="en">
<head>
<meta charset="utf-8">
<title>Brindlewood Property Management – Business Cards</title>
<link href="https://fonts.googleapis.com/css2?family=Open+Sans:wght@400;600;700&display=swap" rel="stylesheet">
<style>
  :root {
    --bg: #e9e7e4;
    --brand-blue: #1c3e94;
    --brand-deep: #0f2466;
    --brand-light: #3f6fd1;
    --sky: #8fb4ef;
    --ink: #333a45;
    --muted: #6b7280;
    --card-white: #ffffff;
    --card-grey-top: #8c8c8c;
    --card-grey-bottom: #6f6f6f;
  }
  * { box-sizing: border-box; margin: 0; padding: 0; }
  html, body { width: 1200px; height: 842px; overflow: hidden; }
  body {
    background: var(--bg);
    font-family: "Open Sans", Arial, sans-serif;
    color: var(--ink);
  }
  .sheet {
    position: relative;
    width: 1200px;
    height: 842px;
    display: grid;
    grid-template-columns: 480px 480px;
    grid-template-rows: 274px 274px;
    gap: 70px 60px;
    justify-content: center;
    align-content: center;
  }
  .card {
    position: relative;
    border-radius: 12px;
    overflow: hidden;
    box-shadow: 0 10px 24px rgba(0,0,0,.18);
  }
  .brand {
    display: flex; align-items: center; gap: 12px;
  }
  .brand-dot {
    border-radius: 50%;
    background: var(--brand-blue);
    flex: none;
  }
  .brand-name {
    font-family: "Open Sans", Arial, sans-serif;
    font-weight: 600;
    color: var(--brand-blue);
    letter-spacing: 1px;
    line-height: 1.2;
  }
  .brand-name small { display: block; font-size: 10px; letter-spacing: 2px; }
  .url {
    font-weight: 600;
    letter-spacing: 2.5px;
    font-size: 13px;
  }

  /* front */
  .card--front { background: var(--card-white); }
  .front-brand { position: absolute; left: 26px; top: 34px; }
  .front-brand .brand-dot { width: 48px; height: 48px; }
  .front-brand .brand-name { font-size: 26px; }
  .holder { position: absolute; right: 28px; top: 136px; }
  .holder-name { color: var(--brand-blue); font-weight: 700; font-size: 17px; }
  .holder-title { font-size: 11px; color: var(--muted); margin-top: 2px; }
  .contact {
    position: absolute; left: 26px; top: 150px;
    font-size: 10.5px; line-height: 1.65; color: var(--ink);
  }
  .contact dt { display: inline-block; width: 42px; color: var(--muted); }
  .contact dd { display: inline; }
  .front-band {
    position: absolute; left: 0; right: 0; bottom: 0; height: 34px;
    background: linear-gradient(180deg, var(--brand-light), var(--brand-deep));
  }
  .front-band::before {
    content: ""; position: absolute; left: 0; right: 0; top: -8px; height: 8px;
    background: linear-gradient(90deg, var(--sky), #dfe9fb);
  }

  /* backs */
  .card--grey { background: linear-gradient(160deg, var(--card-grey-top), var(--card-grey-bottom)); }
  .card--blue { background: radial-gradient(ellipse at 50% 30%, var(--brand-light), var(--brand-deep) 75%); }
  .card--white { background: var(--card-white); }
  .back-brand {
    position: absolute; left: 0; right: 0; top: 92px;
    justify-content: center;
  }
  .back-brand .brand-dot { width: 44px; height: 44px; }
  .back-brand .brand-name { font-size: 23px; }
  .card--grey .brand-dot, .card--blue .brand-dot { background: #ffffff; }
  .card--grey .brand-name, .card--blue .brand-name { color: #ffffff; }
  .card--grey .url { position: absolute; right: 34px; bottom: 30px; color: #fff; }
  .card--blue .url { position: absolute; left: 0; right: 0; bottom: 32px; text-align: center; color: #fff; }
  .card--white .url { position: absolute; left: 0; right: 0; bottom: 32px; text-align: center; color: var(--brand-blue); }
</style>
</head>
<body>
<main class="sheet">
  <section class="card card--front" aria-label="Business card front">
    <div class="brand front-brand">
      <span class="brand-dot"></span>
      <div class="brand-name">BRINDLEWOOD<small>PROPERTY MANAGEMENT</small></div>
    </div>
    <div class="holder">
      <div class="holder-name">Doreen Whitlock,CAM</div>
      <div class="holder-title">President</div>
    </div>
    <dl class="contact">
      <div>P.O. Box 572816 Naples, FL. 34117</div>
      <div><dt>Phone</dt><dd>239.555.0148</dd></div>
      <div><dt>Email</dt><dd>info@brindlewoodprop.com</dd></div>
      <div><dt>Web</dt><dd>www.brindlewoodprop.com</dd></div>
    </dl>
    <div class="front-band"></div>
  </section>

  <section class="card card--grey" aria-label="Business card back, grey">
    <div class="brand back-brand">
      <span class="brand-dot"></span>
      <div class="brand-name">BRINDLEWOOD<small>PROPERTY MANAGEMENT</small></div>
    </div>
    <div class="url">www.brindlewoodprop.com</div>
  </section>

  <section class="card card--blue" aria-label="Business card back, blue">
    <div class="brand back-brand">
      <span class="brand-dot"></span>
      <div class="brand-name">BRINDLEWOOD<small>PROPERTY MANAGEMENT</small></div>
    </div>
    <div class="url">www.brindlewoodprop.com</div>
  </section>

  <section class="card card--white" aria-label="Business card back, white">
    <div class="brand back-brand">
      <span class="brand-dot"></span>
      <div class="brand-name">BRINDLEWOOD<small>PROPERTY MANAGEMENT</small></div>
    </div>
    <div class="url">www.brindlewoodprop.com</div>
  </section>
</main>
</body>
</html>
```